3D printers services needs a brochure

We need a Creative, Innovative idea for a brochure. 3d printing for Prototyping, .
We would like to have an A4 horizontal brochure that could give a 3D effect when folded or cut.
Our name is K7! Gather! Shape! Go! our website is www.k7venturelab.example. Please be inspired by our logo and the dreamy cloud part.
Our prospects: Architects, Artists, Museums and Designers ( Jewellery, watches, etc ...)
What we offer:
.3D printing and prototyping.
.3D scanning.
.Transforming 2D images to 3D objects.
. Making their Portals where clients can visualize, personalize (IN 3D) and order their work.

Reason: I would like to extend it because i figured out the deadline is too short! Thank you Best regards Tarek

```html
<!DOCTYPE html>
<html lang="en">
<head>
<meta charset="utf-8">
<title>K7 Venture Lab – Trifold Brochure</title>
<link rel="stylesheet" href="https://fonts.googleapis.com/css2?family=Bitter:wght@400&family=Didact+Gothic&family=Roboto:wght@400;500&family=Roboto+Condensed:wght@400;700&display=swap">
<style>
:root{
  --page:#ffffff;
  --backdrop:#ececec;
  --fold:#c9c9c9;
  --cyan:#3fd6ea;
  --cyan-btn:#5ee8f4;
  --lime:#86cc16;
  --lime-dark:#5fae10;
  --slate:#6f7a78;
  --ink:#222222;
  --cloud-line:#bfe6f5;
  --logo-grey:#8c9290;
}
*{box-sizing:border-box;margin:0;padding:0}
html,body{width:1200px;height:866px;overflow:hidden;background:var(--backdrop)}
.brochure{position:absolute;left:69px;top:24px;width:1058px;height:823px;overflow:hidden;background:var(--page);box-shadow:0 4px 18px rgba(0,0,0,.18);font-family:'Roboto',Arial,sans-serif;color:var(--ink)}
.fold{position:absolute;top:0;bottom:0;width:1px;background:var(--fold)}
.fold--one{left:357px}.fold--two{left:701px}

/* left panel */
.hero-image{position:absolute;left:25px;top:27px;width:320px;height:378px;background:linear-gradient(150deg,#f1f2f3 0%,#d9dcdd 35%,#9bd42a 55%,#7bbf12 70%,#e6e8e9 100%)}
.prospects{position:absolute;left:28px;top:436px;width:310px;color:var(--cyan);font-size:18.5px;line-height:28px}
.offer-title{position:absolute;left:28px;top:520px;width:145px;color:var(--lime);font-family:'Roboto Condensed',Arial,sans-serif;font-weight:700;font-size:21px;line-height:26px;padding-bottom:1px;border-bottom:1px solid #d8d8d8}
.offer-list{position:absolute;left:36px;top:560px;width:300px;list-style:none;font-size:13.5px;line-height:18px}
.offer-list li{position:relative;padding-left:20px;margin-bottom:11px}
.offer-list li::before{content:"";position:absolute;left:0;top:4px;width:9px;height:9px;border-radius:2px;background:var(--lime)}
.call{position:absolute;border-radius:40px;text-align:center;font-family:'Roboto Condensed',Arial,sans-serif;box-shadow:0 4px 8px rgba(0,0,0,.25)}
.call span{display:block;font-size:19px;line-height:22px}
.call strong{display:block;font-weight:400;font-size:25px;line-height:30px}
.call--cyan{left:35px;top:717px;width:196px;height:79px;background:var(--cyan-btn);color:#111;padding-top:12px}
.call--lime{left:781px;top:721px;width:197px;height:80px;background:linear-gradient(180deg,var(--lime),var(--lime-dark));color:#fff;padding-top:12px}

/* middle panel */
.cloud-quote{position:absolute;left:366px;top:36px;width:334px;height:170px}
.cloud-quote p{position:absolute;left:10px;right:0;top:50px;text-align:center;font-size:18.5px;line-height:28px;color:#222}
.brand{position:absolute;text-align:center}
.brand__name{display:block;font-family:'Roboto',Arial,sans-serif;font-weight:500;color:var(--logo-grey)}
.brand__mark{display:inline-block;background:var(--lime);vertical-align:middle;margin-right:10px}
.brand__tag{display:block;font-family:'Didact Gothic',Arial,sans-serif;color:#333;white-space:nowrap}
.brand--small{left:370px;top:424px;width:170px}
.brand--small .brand__name{font-size:46px;line-height:60px}
.brand--small .brand__mark{width:22px;height:22px}
.brand--small .brand__tag{font-size:13.5px;letter-spacing:.5px;margin-top:36px}
.contact{position:absolute;left:383px;top:566px;width:270px;list-style:none;font-size:13px;line-height:16px}
.contact li{position:relative;padding-left:19px}
.contact svg{position:absolute;left:0;top:1px;width:14px;height:14px}
.contact .gap{margin-top:21px}
.contact .near{margin-top:5px}
.follow{position:absolute;left:374px;top:733px;width:109px;font-size:13px;line-height:16px;padding-bottom:4px;border-bottom:1px solid #cfcfcf}
.social{position:absolute;left:374px;top:762px;display:flex;gap:5px}
.social span{width:25px;height:25px;border-radius:50%;background:#2f7fd0;border:2px solid #222}

/* right panel */
.brand--large{left:717px;top:78px;width:300px}
.brand--large .brand__name{font-size:98px;line-height:120px}
.brand--large .brand__mark{width:40px;height:40px}
.brand--large .brand__tag{font-size:24px;letter-spacing:1.5px;margin-top:40px}
.expertise{position:absolute;left:712px;top:316px;width:310px;text-align:center;font-family:'Bitter',Georgia,serif;font-size:26px;line-height:39px;color:var(--slate)}
.scene-cloud{position:absolute;left:529px;top:505px;width:516px;height:296px}
</style>
</head>
<body>
<div class="brochure">
  <div class="fold fold--one"></div>
  <div class="fold fold--two"></div>

  <!-- Left panel -->
  <div class="hero-image" role="img" aria-label="3D architectural model of a floor plan with lime green walls over blueprint drawings"></div>
  <p class="prospects">Our prospects: Architects,<br>Artists, Museums and Designers</p>
  <h2 class="offer-title">What we offer:</h2>
  <ul class="offer-list">
    <li>3D printing and prototyping</li>
    <li>3D scanning</li>
    <li>Transforming 2D images to 3D objects</li>
    <li>Making their Portals where clients can<br>visualize, personalize (IN 3D) and order<br>their work</li>
  </ul>
  <div class="call call--cyan"><span>Call Us Today</span><strong>4155-010-2233</strong></div>

  <!-- Middle panel -->
  <div class="cloud-quote">
    <svg width="334" height="170" viewBox="0 0 334 170" aria-hidden="true">
      <path d="M40 160 C10 160 2 130 20 114 C5 95 25 70 50 78 C55 50 90 42 108 58 C120 20 170 8 195 32 C215 12 255 20 255 55 C285 45 315 65 305 95 C332 105 330 158 295 160 Z" fill="#fff" stroke="var(--cloud-line)" stroke-width="3"/>
    </svg>
    <p>We act<br>as your consultants<br>to offer the best tools needed<br>for your 3D projects.</p>
  </div>

  <div class="brand brand--small">
    <span class="brand__name"><i class="brand__mark"></i>K7</span>
    <span class="brand__tag">GATHER! SHAPE! GO!</span>
  </div>

  <ul class="contact">
    <li><svg viewBox="0 0 14 14"><path d="M7 1a4 4 0 0 1 4 4c0 3-4 8-4 8S3 8 3 5a4 4 0 0 1 4-4z" fill="var(--lime)"/><circle cx="7" cy="5" r="1.5" fill="#fff"/></svg>Rue des Lilas 8, Lausanne 1003<br>Switzerland</li>
    <li class="gap"><svg viewBox="0 0 14 14"><rect x="1" y="3" width="12" height="8" fill="none" stroke="var(--lime)" stroke-width="1.5"/><path d="M1 3l6 5 6-5" fill="none" stroke="var(--lime)" stroke-width="1.5"/></svg>Tarek@k7venturelab.example</li>
    <li class="near"><svg viewBox="0 0 14 14"><circle cx="7" cy="7" r="5.5" fill="none" stroke="var(--lime)" stroke-width="1.3"/><ellipse cx="7" cy="7" rx="2.3" ry="5.5" fill="none" stroke="var(--lime)" stroke-width="1.1"/><path d="M1.5 7h11" stroke="var(--lime)" stroke-width="1.1"/></svg>www.k7venturelab.example</li>
    <li class="gap"><svg viewBox="0 0 14 14"><circle cx="7" cy="7" r="6" fill="none" stroke="var(--lime)" stroke-width="1.3"/><path d="M5 4l1.5 2-1 1c.5 1 1 1.5 2 2l1-1 2 1.5-1 1.5C6 11 3.5 8 4 5z" fill="var(--lime)"/></svg>4155 010 2233</li>
    <li class="near"><svg viewBox="0 0 14 14"><rect x="3" y="1.5" width="8" height="4" fill="none" stroke="var(--lime)" stroke-width="1.3"/><rect x="1.5" y="5.5" width="11" height="5" fill="var(--lime)"/><rect x="3.5" y="9" width="7" height="3.5" fill="#fff" stroke="var(--lime)" stroke-width="1.2"/></svg>4155 010 2233</li>
  </ul>
  <p class="follow">Follow Us On</p>
  <div class="social" aria-label="Social media links"><span></span><span></span><span></span></div>

  <!-- Right panel -->
  <div class="brand brand--large">
    <span class="brand__name"><i class="brand__mark"></i>K7</span>
    <span class="brand__tag">GATHER! SHAPE! GO!</span>
  </div>
  <p class="expertise">We Are Experts In<br>3d Designing,<br>Scanning &amp;<br>Printing Technologies.</p>

  <svg class="scene-cloud" viewBox="0 0 520 300" preserveAspectRatio="none" role="img" aria-label="Child reaching up toward hand-drawn sketches of ideas and gadgets on a grey wall, shaped as a cloud">
    <defs>
      <linearGradient id="sceneTone" x1="0" y1="0" x2="0" y2="1">
        <stop offset="0" stop-color="#e4e6e5"/>
        <stop offset=".7" stop-color="#c9cccb"/>
        <stop offset="1" stop-color="#a9adab"/>
      </linearGradient>
    </defs>
    <path d="M30 300 C5 285 0 240 20 222 C8 190 30 160 62 168 C70 130 110 115 138 132 C150 70 215 50 250 80 C270 20 345 5 385 40 C420 10 480 30 480 80 C515 95 520 150 505 175 C520 205 518 260 500 300 Z" fill="url(#sceneTone)"/>
  </svg>
  <div class="call call--lime"><span>Call Us Today</span><strong>4155-010-2233</strong></div>
</div>
</body>
</html>
```